Carte d'affaire bilingue

Nous avons besoin d'une carte d'affaire pour notre entreprise spécialisée en vente et achat de terrain. Nous sommes une agence immobilière et nous voulons une carte avec le recto en Français et le verso en anglais. Nous voulons une image sobre et épurée. Nous avons de la clientèle internationale et nous voulons une carte très professionnelle mais qui se démarque. Nous voulons cibler une clientèle commerciale, industrielle, contracteurs et promoteurs immobiliers.

Hi everybody, we saw all your conception and we are approching of what we like but the "WOW" is missing.

We love the little sign to specify (phone or email) but we can put them in a square to make like our logo, we love also dark gray not lite gray, we also love the stainless lines. In our logo you can see a little sign +. For us is signyfy " Always further" so if you can put many little +++++ in the conception somewhere very discret it will be appreciate. We also like a kind of round that make a magnyfying glass, because we search land we found opportunity.

Thank you

Reason: I ask different things in the last day but no one do what i am asking for. For the conception # 3016702 that we love we ask changes.

We like simplicity, urban design, corporate, international. The card must have one side in french and the other side in english. We like dark gray,silver, and a little bit of green.

Target Market(s)

Investors, developers, construction builders, etc...

Font styles to use
Serif
Sans Serif

Requirements
Must have
• logo
La mention: Agence immobilière (Francais) / Real Estate Agency (anglais)
Sous le nom: Courtier immobilier agréé (Français) / Real Estate Broker

```html
<!DOCTYPE html>
<html lang="fr">
<head>
<meta charset="utf-8">
<title>Carte d'affaires bilingue</title>
<link href="https://fonts.googleapis.com/css2?family=Marcellus&family=Lato:wght@400;700&display=swap" rel="stylesheet">
<style>
  :root {
    --bg-top: #d9d9d9;
    --bg-bottom: #c4c4c4;
    --card: #ffffff;
    --green: #0b7a3b;
    --green-dark: #06652f;
    --ink: #3a3a3a;
    --label: #2d9a55;
    --soft: #6e6e6e;
  }
  * { margin: 0; padding: 0; box-sizing: border-box; }
  html, body { width: 1200px; height: 750px; overflow: hidden; }
  body {
    background: linear-gradient(160deg, var(--bg-top), var(--bg-bottom));
    display: flex;
    align-items: center;
    justify-content: center;
    gap: 60px;
    font-family: "Lato", Arial, sans-serif;
  }
  .card {
    position: relative;
    width: 500px;
    height: 286px;
    background: var(--card);
    border-radius: 26px;
    overflow: hidden;
    box-shadow: 0 10px 24px rgba(0,0,0,.18);
  }
  .brand {
    position: absolute;
    left: 26px;
    top: 54px;
    display: flex;
    align-items: center;
    gap: 12px;
  }
  .brand-square {
    width: 44px;
    height: 44px;
    background: var(--green);
  }
  .brand-text { display: flex; flex-direction: column; }
  .brand-name {
    font-family: "Marcellus", Georgia, serif;
    font-size: 24px;
    line-height: 1;
    color: var(--ink);
    letter-spacing: .5px;
  }
  .brand-agency {
    font-family: "Marcellus", Georgia, serif;
    font-size: 11px;
    color: var(--soft);
    margin-top: 4px;
  }
  .brand-tagline {
    font-size: 7px;
    color: var(--soft);
    margin-top: 2px;
  }
  .name-band {
    position: absolute;
    left: 0;
    right: 0;
    top: 112px;
    height: 62px;
    background: linear-gradient(90deg, var(--green-dark), var(--green));
    color: #fff;
    text-align: center;
    padding-left: 150px;
    padding-top: 10px;
  }
  .person-name {
    font-size: 25px;
    letter-spacing: 1px;
    line-height: 1.1;
  }
  .person-title {
    font-family: "Marcellus", Georgia, serif;
    font-size: 11px;
    opacity: .9;
  }
  .contact {
    position: absolute;
    right: 30px;
    top: 190px;
    text-align: right;
    font-size: 12.5px;
    line-height: 1.45;
    color: var(--ink);
  }
  .contact-label { color: var(--label); font-weight: 700; }
</style>
</head>
<body>

  <article class="card card-fr" lang="fr">
    <div class="brand">
      <span class="brand-square"></span>
      <div class="brand-text">
        <span class="brand-name">Le Repère Foncier</span>
        <span class="brand-agency">Agence immobilière</span>
        <span class="brand-tagline">Terrains commerciaux et industriels</span>
      </div>
    </div>
    <div class="name-band">
      <p class="person-name">NOM PRENOM</p>
      <p class="person-title">Courtier immobilier agréé</p>
    </div>
    <div class="contact">
      <p><span class="contact-label">Adresse:</span> 27 B, rue des Érables, Laval, Qc, H7M 4K2</p>
      <p><span class="contact-label">email:</span> j.tremblay@reperefoncier.com - <span class="contact-label">web site:</span> www.reperefoncier.com</p>
      <p><span class="contact-label">phone number:</span> 514-555-0148 - <span class="contact-label">fax:</span> 450-555-0193</p>
      <p><span class="contact-label">toll free:</span> 1-866-555-0110</p>
    </div>
  </article>

  <article class="card card-en" lang="en">
    <div class="brand">
      <span class="brand-square"></span>
      <div class="brand-text">
        <span class="brand-name">Land Compass</span>
        <span class="brand-agency">Real Estate Agency</span>
        <span class="brand-tagline">Commercial and industrial land</span>
      </div>
    </div>
    <div class="name-band">
      <p class="person-name">NOM PRENOM</p>
      <p class="person-title">Real Estate Broker</p>
    </div>
    <div class="contact">
      <p><span class="contact-label">Adresse:</span> 27 B, rue des Érables, Laval, Qc, H7M 4K2</p>
      <p><span class="contact-label">email:</span> j.tremblay@reperefoncier.com - <span class="contact-label">web site:</span> www.reperefoncier.com</p>
      <p><span class="contact-label">phone number:</span> 514-555-0148 - <span class="contact-label">fax:</span> 450-555-0193</p>
      <p><span class="contact-label">toll free:</span> 1-866-555-0110</p>
    </div>
  </article>

</body>
</html>
```